Veridan Crest Business Cards

Veridan Crest Prestige Portfolio Group is a global representation business focusing on high end luxury. We need business cards to epitomize our global, luxury delivery model.

Target Market(s)

Global Representation in the hospitality industry

Industry/Entity Type

Hospitality

Contact Information for Business Card

name
title
email: first.last@vc-ppg.com
web: www.vc-ppg.com
mobile:

Requirements
Must have
• double sided design
• incorporate logo colours
• have logo prominent
Should not have
• no designs not incorporating logo colours.

```html
<!DOCTYPE html>
<html lang="en">
<head>
<meta charset="utf-8">
<title>Veridan Crest Business Cards</title>
<link href="https://fonts.googleapis.com/css2?family=Cinzel:wght@400;500&family=Roboto:wght@400;500&display=swap" rel="stylesheet">
<style>
  :root {
    --backdrop: #93a3ab;
    --gold: #806b3e;
    --gold-soft: #8f7a4e;
    --paper: #ffffff;
    --ink: #1c1c1c;
  }
  * { margin: 0; padding: 0; box-sizing: border-box; }
  html, body { width: 1200px; height: 900px; overflow: hidden; }
  body {
    background: var(--backdrop);
    position: relative;
    font-family: "Roboto", Arial, sans-serif;
  }
  .card {
    position: absolute;
    width: 620px;
    height: 354px;
    border-radius: 22px;
    box-shadow: 0 10px 24px rgba(0,0,0,0.25);
  }
  .card-front {
    left: 80px; top: 60px;
    background: var(--gold);
    display: flex; flex-direction: column;
    align-items: center; justify-content: center;
    color: var(--paper);
    font-family: "Cinzel", Georgia, serif;
    font-weight: 400;
    text-align: center;
  }
  .front-name { font-size: 40px; letter-spacing: 4px; }
  .front-sub { font-size: 20px; letter-spacing: 3px; margin-top: 8px; }
  .card-back {
    left: 500px; top: 486px;
    background: var(--paper);
    color: var(--ink);
  }
  .brand {
    position: absolute; left: 44px; top: 96px;
    font-family: "Cinzel", Georgia, serif; font-weight: 500;
    color: var(--gold);
  }
  .brand-mark {
    display: inline-block; width: 14px; height: 14px;
    background: var(--gold); margin-right: 8px; vertical-align: middle;
  }
  .brand-name { font-size: 30px; vertical-align: middle; }
  .brand-sub { font-size: 10.5px; letter-spacing: 1.6px; margin-top: 6px; }
  .divider {
    position: absolute; left: 40px; top: 192px;
    width: 400px; height: 2px; background: var(--gold);
  }
  .person { position: absolute; right: 40px; top: 152px; text-align: left; }
  .person-name { font-size: 20px; font-weight: 500; color: var(--gold); letter-spacing: 0.3px; }
  .person-title { font-size: 12px; margin-top: 2px; }
  .address {
    position: absolute; right: 40px; top: 232px;
    font-size: 14px; line-height: 1.35; text-align: right;
  }
  .contacts { position: absolute; left: 52px; top: 214px; list-style: none; }
  .contacts li {
    display: flex; align-items: center; gap: 14px;
    font-size: 15px; height: 26px;
  }
  .contact-icon {
    width: 20px; height: 20px; background: var(--gold);
    display: flex; align-items: center; justify-content: center;
  }
</style>
</head>
<body>
  <section class="card card-front" aria-label="Card front">
    <div class="front-name">VERIDAN CREST</div>
    <div class="front-sub">PRESTIGE PORTFOLIO GROUP</div>
  </section>

  <section class="card card-back" aria-label="Card back">
    <div class="brand">
      <div><span class="brand-mark"></span><span class="brand-name">Veridan Crest</span></div>
      <div class="brand-sub">PRESTIGE PORTFOLIO GROUP</div>
    </div>

    <div class="person">
      <div class="person-name">ELIAS MARLOWE</div>
      <div class="person-title">Founder &amp; Director</div>
    </div>

    <div class="divider"></div>

    <div class="address">48 Harbor Row - Linden<br>Northvale 20418</div>

    <ul class="contacts">
      <li>
        <span class="contact-icon">
          <svg width="12" height="12" viewBox="0 0 12 12"><path d="M2.5 1 L4.5 1 L5.3 3.5 L4 4.5 Q5 7 7.5 8 L8.5 6.7 L11 7.5 L11 9.5 Q10 11 8.5 11 Q1 10 1 3.5 Q1 2 2.5 1 Z" fill="#fff"/></svg>
        </span>
        555-010-2034
      </li>
      <li>
        <span class="contact-icon">
          <svg width="12" height="12" viewBox="0 0 12 12"><path d="M1 4 Q6 0 11 4 L11 5 L8.5 5 L8.5 4 Q6 3 3.5 4 L3.5 5 L1 5 Z" fill="#fff"/><rect x="2.5" y="6" width="7" height="5" rx="1" fill="#fff"/></svg>
        </span>
        555-010-7781
      </li>
      <li>
        <span class="contact-icon">
          <svg width="12" height="12" viewBox="0 0 12 12"><rect x="1" y="2.5" width="10" height="7" fill="none" stroke="#fff" stroke-width="1.2"/><path d="M1 2.5 L6 7 L11 2.5" fill="none" stroke="#fff" stroke-width="1.2"/></svg>
        </span>
        first.last@vc-ppg.com
      </li>
      <li>
        <span class="contact-icon">
          <svg width="12" height="12" viewBox="0 0 12 12"><circle cx="6" cy="6" r="4.8" fill="none" stroke="#fff" stroke-width="1.1"/><ellipse cx="6" cy="6" rx="2" ry="4.8" fill="none" stroke="#fff" stroke-width="1"/><line x1="1.2" y1="6" x2="10.8" y2="6" stroke="#fff" stroke-width="1"/></svg>
        </span>
        www.vc-ppg.com
      </li>
    </ul>
  </section>
</body>
</html>
```